BriarLoom Website Homepage Design

Please provide your idea of homepage for a hosting company. This project is for DESIGN only, no coding.

It must use/combine colors used in logo, clean, modern look.

Homepage must consist of at least 4 sections (example: testimonials, services, and so on. not necesarily all of them). We would like the navigation to be horizontal, but not mandatory.

You can include a preview of services page (optional, not a must).

Number of Pages Required

1 page

Font styles to use
Sans Serif

```html
<!DOCTYPE html>
<html lang="en">
<head>
<meta charset="UTF-8">
<title>BriarLoom — Hosting Company</title>
<link href="https://fonts.googleapis.com/css2?family=Poppins:wght@300;400;500;600;700;800&display=swap" rel="stylesheet">
<style>
:root{
  --navy:#0b4a92;
  --blue:#1479d2;
  --sky:#1e93e6;
  --accent:#49c6ff;
  --aqua:#7fdcf2;
  --mist:#d8f3f5;
  --white:#ffffff;
  --ink:#111827;
  --grey:#7b8794;
}
*{margin:0;padding:0;box-sizing:border-box}
html,body{width:1200px;height:1097px;overflow:hidden}
body{font-family:'Poppins',sans-serif;background:var(--mist);position:relative;color:var(--ink)}

.hero{position:absolute;left:0;top:0;width:1200px;height:470px;
  background:linear-gradient(120deg,var(--navy) 0%,var(--blue) 55%,var(--sky) 100%);overflow:hidden}
.hero-waves{position:absolute;left:0;bottom:0;width:1200px;height:120px}

.nav{position:absolute;top:30px;left:100px;right:110px;display:flex;align-items:center;justify-content:space-between}
.brand{display:flex;align-items:center;gap:10px;color:var(--white);font-weight:600;font-size:28px;letter-spacing:2px;line-height:1.2}
.brand-dot{width:14px;height:14px;border-radius:50%;background:var(--white)}
.nav-links{display:flex;align-items:center;gap:36px;list-style:none}
.nav-links a{color:var(--white);text-decoration:none;font-size:13px;font-weight:500}
.nav-links .cta{background:var(--white);color:var(--blue);padding:9px 22px;border-radius:20px}

.hero-copy{position:absolute;left:110px;top:125px;width:460px;color:var(--white)}
.hero-kicker{font-size:38px;font-weight:300;line-height:1.2}
.hero-title{font-size:46px;font-weight:700;line-height:1.2}
.hero-title span{color:var(--accent)}
.hero-text{font-size:13px;line-height:1.7;margin-top:12px;max-width:440px}
.btn-outline{display:inline-block;margin-top:20px;border:1.5px solid var(--white);color:var(--white);
  font-size:12px;font-weight:600;padding:8px 28px;border-radius:20px;text-decoration:none}
.hero-art{position:absolute;left:680px;top:80px;width:360px;height:280px;border-radius:30px;
  background:radial-gradient(circle at 55% 45%,#4fe0ff 0%,#2f6ee0 45%,rgba(40,90,200,0) 75%)}

.services{position:absolute;left:0;top:470px;width:1200px;padding-top:22px;text-align:center}
.section-title{font-size:40px;font-weight:700;line-height:1.2;color:var(--ink)}
.service-grid{display:grid;grid-template-columns:repeat(3,300px);justify-content:center;margin-top:16px;row-gap:6px}
.service{padding:14px 20px;height:136px;border-radius:40px}
.service.featured{background:var(--white);box-shadow:0 10px 30px rgba(20,90,150,.12)}
.service-icon{width:34px;height:34px;margin:0 auto;border-radius:10px;
  background:linear-gradient(135deg,var(--sky),var(--accent))}
.service h3{font-size:14px;font-weight:600;line-height:1.5;margin-top:10px}
.service p{font-size:11.5px;color:var(--grey);line-height:1.6;margin-top:6px}

.about{position:absolute;left:145px;top:850px;width:910px;height:230px;background:var(--white);
  border-radius:44px;box-shadow:0 10px 40px rgba(20,90,150,.12);padding:34px 88px}
.about h2{font-size:38px;font-weight:700;line-height:1.2}
.about p{font-size:12px;color:#4b5563;line-height:1.65;width:480px;margin-top:12px}
.btn-solid{display:inline-block;margin-top:16px;background:var(--sky);color:var(--white);font-size:12px;
  font-weight:600;padding:8px 26px;border-radius:20px;text-decoration:none}
.about-art{position:absolute;right:60px;top:35px;width:260px;height:160px;border-radius:24px;
  background:linear-gradient(135deg,#d9e8ff,#7fb3f0)}

.blob{position:absolute}
</style>
</head>
<body>

<header class="hero">
  <nav class="nav">
    <div class="brand"><span class="brand-dot"></span>BRIARLOOM</div>
    <ul class="nav-links">
      <li><a href="#">Home</a></li>
      <li><a href="#">About Us</a></li>
      <li><a href="#">Services</a></li>
      <li><a href="#">FAQ</a></li>
      <li><a href="#">Testimonials</a></li>
      <li><a href="#" class="cta">Contact Us</a></li>
    </ul>
  </nav>

  <div class="hero-copy">
    <p class="hero-kicker">Hosting Company</p>
    <h1 class="hero-title"><span>Large</span> Database</h1>
    <p class="hero-text">Contrary to popular belief, Lorem Ipsum is not simply random text. It has roots in a piece of classical Latin literature from</p>
    <a href="#" class="btn-outline">Register</a>
  </div>

  <div class="hero-art" role="img" aria-label="Isometric illustration of glowing server racks on a circuit board"></div>

  <svg class="hero-waves" viewBox="0 0 1200 120" preserveAspectRatio="none" aria-hidden="true">
    <path d="M0 40 C120 15 220 60 340 40 C470 15 560 55 700 35 C830 15 930 50 1050 30 C1120 20 1170 30 1200 35 L1200 120 L0 120Z" fill="#3fb0ea" opacity=".7"/>
    <path d="M0 65 C140 45 240 85 380 65 C520 45 600 80 760 60 C900 40 1000 75 1120 60 C1160 55 1185 58 1200 60 L1200 120 L0 120Z" fill="#7fdcf2" opacity=".85"/>
    <path d="M0 95 C160 78 260 108 420 90 C560 76 660 105 820 88 C960 74 1060 100 1200 85 L1200 120 L0 120Z" fill="#d8f3f5"/>
  </svg>
</header>

<svg class="blob" style="left:-20px;top:640px" width="110" height="170" viewBox="0 0 110 170" aria-hidden="true">
  <path d="M10 10 C70 0 100 50 80 90 C60 130 20 120 0 100Z" fill="#0b5fc0"/>
  <path d="M0 90 C50 80 70 130 40 160 C20 175 0 160 0 150Z" fill="#22a7e6"/>
  <circle cx="95" cy="140" r="6" fill="#0b5fc0"/>
</svg>
<svg class="blob" style="left:1120px;top:560px" width="80" height="150" viewBox="0 0 80 150" aria-hidden="true">
  <path d="M80 0 C30 5 0 50 10 90 C20 130 60 145 80 140Z" fill="#0a6fd0"/>
  <circle cx="72" cy="12" r="4" fill="none" stroke="#ffffff" stroke-width="1.5"/>
</svg>

<section class="services">
  <h2 class="section-title">Our Services</h2>
  <div class="service-grid">
    <article class="service">
      <div class="service-icon" role="img" aria-label="Database icon"></div>
      <h3>Large Database</h3>
      <p>Contrary to popular belief, Lorem Ipsum is not simply random text.</p>
    </article>
    <article class="service featured">
      <div class="service-icon" role="img" aria-label="Web server globe icon"></div>
      <h3>Web Server</h3>
      <p>Contrary to popular belief, Lorem Ipsum is not simply random text.</p>
    </article>
    <article class="service">
      <div class="service-icon" role="img" aria-label="Networking icon"></div>
      <h3>Networking</h3>
      <p>Contrary to popular belief, Lorem Ipsum is not simply random text.</p>
    </article>
    <article class="service">
      <div class="service-icon" role="img" aria-label="Cloud computing icon"></div>
      <h3>Cloud Computing</h3>
      <p>Contrary to popular belief, Lorem Ipsum is not simply random text.</p>
    </article>
    <article class="service">
      <div class="service-icon" role="img" aria-label="Hosting domain icon"></div>
      <h3>Hosting Domain</h3>
      <p>Contrary to popular belief, Lorem Ipsum is not simply random text.</p>
    </article>
    <article class="service">
      <div class="service-icon" role="img" aria-label="SEO search icon"></div>
      <h3>SEO</h3>
      <p>Contrary to popular belief, Lorem Ipsum is not simply random text.</p>
    </article>
  </div>
</section>

<section class="about">
  <h2>About Us</h2>
  <p>Consectetur blandit sem faucibus dignissim. Interdum et malesuada fames ac ante ipsum primis in faucibus. Phasellus tincidunt vulputate dolor nec varius. Phasellus eget tincidunt turpis. Donec ut mauris iaculis.</p>
  <a href="#" class="btn-solid">View More</a>
  <div class="about-art" role="img" aria-label="Isometric illustration of a laptop beside a server tower and cloud"></div>
</section>

</body>
</html>
```